A singer "Vemaru" needs a CD cover artwork

My name is "Vemaru". I need a CD cover artwork for my first EP named "Hold Fast". The cover needs to be just a digital artwork at this moment. It requires to contain the print of "Vemaru" and "Hold Fast" somewhere in front. And the image will be like a man alone standing in a big city (Tokyo, hopefully) with no one around in a morning sun rising. I am thinking about the artwork of novels of Ron Marsh (Wade Callum series).

A .jpg file is needed.

I have updated this project as non-refundable from 6 March, therefore, I am keen to buy one.

Thank you.

Target Market(s)

Music fans

Industry/Entity Type

Music Download

Colors

Designer to choose colors to be used in the design.

Requirements
Must have
• It requires to contain the print of "Vemaru" and "Hold Fast" somewhere in front.
• A .jpg file is needed.
Nice to have
• And the image will be like a man alone standing in a big city (Tokyo, hopefully) with no one around in a morning sun rising. I am thinking about the artwork of novels of Ron Marsh (Wade Callum series).
• 1. The man standing is not a business man wearing a neat suit, not a youth wearing sneaker shoes, but a man like a Wade Callum, casual style wild.
• 2.Speaking of Wade Callum, please refer to there two designs as they are very close to my idea:
• -Kestrel
• -Flintlock
• 3. The scene of Tokyo doesn't necessary need to be Tokyo. No need of putting real image of Tokyo or Japanese language.
• 4. My songs are design to be soulful and inspiring, therefore, the CD cover design to be something hopeful image please. A man in hope facing the big city and morning sun rising.

```html
<!DOCTYPE html>
<html lang="en">
<head>
<meta charset="utf-8">
<title>Vemaru – Hold Fast</title>
<link rel="stylesheet" href="https://fonts.googleapis.com/css2?family=Anton&family=Josefin+Sans:ital,wght@1,100;1,200&display=swap">
<style>
  :root {
    --sun-yellow: #ffd400;
    --sky-orange: #ff7a0a;
    --sky-deep: #e0420a;
    --haze-red: #c2260a;
    --city-dark: #5e0c06;
    --city-night: #2e0402;
    --title-left: #c72a08;
    --title-right: #ff8a10;
    --title-stroke: #3a0603;
    --subtitle: #ffffff;
  }
  html, body {
    margin: 0;
    padding: 0;
    width: 1200px;
    height: 1200px;
    overflow: hidden;
    background: var(--city-night);
  }
  .cover {
    position: relative;
    width: 1200px;
    height: 1200px;
    overflow: hidden;
  }
  .cityscape-photo {
    position: absolute;
    inset: 0;
    background:
      radial-gradient(circle at 2% 22%, rgba(255,220,0,0.95) 0, rgba(255,180,0,0.6) 12%, rgba(255,140,0,0) 38%),
      radial-gradient(ellipse 70% 10% at 40% 40%, rgba(255,200,40,0.55), rgba(255,200,40,0) 100%),
      linear-gradient(180deg,
        var(--sky-deep) 0%,
        var(--sky-orange) 25%,
        #ff9a10 40%,
        #ff8a0c 47%,
        var(--haze-red) 60%,
        #8e1606 75%,
        var(--city-dark) 88%,
        var(--city-night) 100%);
  }
  .cover-type {
    position: absolute;
    inset: 0;
  }
  .artist-name {
    font-family: "Anton", "Impact", sans-serif;
    font-size: 462px;
    fill: url(#titleFill);
    stroke: var(--title-stroke);
    stroke-width: 1.6;
  }
  .ep-title {
    font-family: "Josefin Sans", sans-serif;
    font-style: italic;
    font-weight: 100;
    font-size: 88px;
    font-variant: small-caps;
    letter-spacing: 2px;
    fill: var(--subtitle);
  }
</style>
</head>
<body>
  <main class="cover">
    <div class="cityscape-photo" role="img" aria-label="Aerial view of a big city skyline with towers silhouetted against a glowing orange sunrise, the sun low on the left and haze over distant hills"></div>
    <svg class="cover-type" width="1200" height="1200" viewBox="0 0 1200 1200">
      <defs>
        <linearGradient id="titleFill" x1="0" y1="0" x2="1" y2="0">
          <stop offset="0" stop-color="var(--title-left)"/>
          <stop offset="1" stop-color="var(--title-right)"/>
        </linearGradient>
      </defs>
      <text class="artist-name" x="34" y="884" textLength="1132" lengthAdjust="spacingAndGlyphs">VEMARU</text>
      <text class="ep-title" x="600" y="1028" text-anchor="middle">Hold Fast</text>
    </svg>
  </main>
</body>
</html>
```